Golf Day Flyer - Harlowe School

Flyer for a golf day.
Parents and friends of a school are invited to play golf on Monday 22nd October.

Flyer from last year (2017) is attached. We would like to make the flyer more fun/humorous this year.

The golf day has two sessions: (1) Round of golf starting at 9AM and (2) Golf Clinic for beginner golfers.

So the flyer could have two sections - one showing experienced golfers, the other showing beginner golfers.

We have not finalised all the content for the flyer yet but need to look at some designs before we give all the content.

Target Market(s)

parents and friends of the school students - professionals (accountants, lawyers, doctors, etc)

Industry/Entity Type

Golf Course

Font styles to use
Serif

Colors

Designer to choose colors to be used in the design.

Requirements
Must have
• Refer to content attached document
Nice to have
• Funny golf pictures
Should not have
• N/A

```html
<!DOCTYPE html>
<html lang="en">
<head>
<meta charset="utf-8">
<title>Harlowe Golf Day 2018</title>
<link rel="stylesheet" href="https://fonts.googleapis.com/css2?family=Oswald:wght@500;600&family=Montserrat:wght@500;600;700&family=Fredoka:wght@600&display=swap">
<style>
  :root {
    --page-bg: #e6e6e4;
    --paper: #ffffff;
    --title-green: #4b7a2a;
    --wave-green: #5e8a31;
    --wave-light: #a3c65a;
    --pill-green: #1f6b3a;
    --frame-green: #3a6a22;
    --ink: #1d1d1b;
    --navy: #174a86;
    --bright-blue: #2473bb;
    --mid-blue: #1d5c9e;
    --olive: #8a7a14;
    --band-blue: #0a6eac;
    --ring-grey: #d6d6d6;
  }
  * { margin: 0; padding: 0; box-sizing: border-box; }
  html, body {
    width: 1200px; height: 1200px; overflow: hidden;
    background: var(--page-bg);
  }
  .flyer {
    position: absolute;
    left: 186px; top: 20px;
    width: 870px; height: 1220px;
    transform: scale(0.951);
    transform-origin: top left;
    background: var(--paper);
    overflow: hidden;
    box-shadow: 0 6px 22px rgba(0,0,0,0.18);
    font-family: "Montserrat", sans-serif;
  }
  .hero-photo {
    position: absolute; left: 0; top: 0;
    width: 870px; height: 700px;
    background:
      radial-gradient(ellipse 420px 260px at 520px 250px, rgba(255,236,170,0.85), rgba(255,236,170,0) 70%),
      linear-gradient(180deg, #f3f1dc 0%, #ece3b0 22%, #cdbb5e 45%, #96a43c 65%, #5f7f2a 100%);
  }
  .wave-art { position: absolute; left: 0; top: 0; width: 870px; height: 1220px; }
  .event-title {
    position: absolute; right: 45px; top: 42px;
    text-align: right;
    font-family: "Oswald", sans-serif; font-weight: 600;
    color: var(--title-green);
    font-size: 90px; line-height: 84px;
    letter-spacing: 1px;
  }
  .venue {
    position: absolute; right: 47px; top: 228px;
    font-weight: 700; font-size: 29px; color: var(--ink);
    letter-spacing: 0.5px;
  }
  .badge {
    position: absolute; left: 479px; top: 370px;
    width: 320px; height: 320px; border-radius: 50%;
    background: var(--paper);
    border: 6px solid var(--ring-grey);
    box-shadow: inset 0 0 18px rgba(0,0,0,0.18), 0 4px 10px rgba(0,0,0,0.15);
    text-align: center;
  }
  .badge-fun {
    margin-top: 92px;
    font-family: "Fredoka", sans-serif; font-weight: 600;
    font-size: 78px; line-height: 72px; color: var(--title-green);
  }
  .badge-day {
    font-family: "Oswald", sans-serif; font-weight: 600;
    font-size: 64px; line-height: 66px; color: var(--navy);
  }
  .function-note {
    position: absolute; left: 51px; top: 634px;
    font-weight: 500; font-size: 19.5px; line-height: 24px;
    color: #ffffff;
  }
  .event-date {
    position: absolute; left: 0; width: 870px; top: 828px;
    text-align: center;
    font-family: "Oswald", sans-serif; font-weight: 600;
    font-size: 60px; line-height: 70px; letter-spacing: 0.5px;
  }
  .event-date .day, .event-date .year { color: var(--navy); }
  .event-date .num { color: var(--bright-blue); }
  .event-date .month { color: var(--mid-blue); }
  .arrival {
    position: absolute; left: 0; width: 870px; top: 910px;
    text-align: center; font-weight: 700; font-size: 27px; color: var(--olive);
  }
  .sessions {
    position: absolute; left: 95px; top: 981px;
    width: 715px; height: 114px;
    border: 2px solid var(--frame-green); border-radius: 16px;
  }
  .session { position: absolute; top: -16px; width: 284px; text-align: center; }
  .session-experienced { left: 32px; }
  .session-beginner { left: 401px; top: -12px; }
  .session-label {
    display: block;
    background: var(--pill-green); color: #ffffff;
    border-radius: 14px;
    font-weight: 700; font-size: 20.5px; line-height: 38px;
    letter-spacing: -0.2px;
  }
  .session-detail {
    margin-top: 10px;
    font-weight: 500; font-size: 18px; line-height: 23px; color: var(--ink);
  }
  .save-band {
    position: absolute; left: 0; top: 1128px;
    width: 870px; height: 92px;
    background: var(--band-blue);
    color: #ffffff; text-align: center;
    font-weight: 700; font-size: 33px; line-height: 92px;
  }
</style>
</head>
<body>
  <main class="flyer">
    <div class="hero-photo" role="img" aria-label="Golf ball on a tee in sunlit grass beside the face of a golf club"></div>

    <svg class="wave-art" viewBox="0 0 870 1220" aria-hidden="true">
      <defs>
        <linearGradient id="waveFill" x1="0" y1="0" x2="1" y2="0">
          <stop offset="0" stop-color="#5c8a2f"/>
          <stop offset="0.5" stop-color="#8bb548"/>
          <stop offset="1" stop-color="#5a8730"/>
        </linearGradient>
      </defs>
      <path d="M0,700 L0,1220 L870,1220 L870,800 C800,720 740,680 680,668 C500,660 300,720 0,755 Z" fill="#ffffff"/>
      <path d="M0,545 C140,615 330,610 500,535 C650,470 760,400 870,390 L870,790 C800,720 740,680 680,668 C520,650 300,720 0,748 Z" fill="url(#waveFill)"/>
      <path d="M0,762 C250,735 420,680 560,655" fill="none" stroke="#2a2a2a" stroke-width="3"/>
      <path d="M700,676 C760,700 820,745 870,800" fill="none" stroke="#2a2a2a" stroke-width="2"/>
      <path d="M0,545 C140,615 330,610 500,535 C650,470 760,400 870,390" fill="none" stroke="#ffffff" stroke-width="4"/>
    </svg>

    <h1 class="event-title">HARLOWE<br>GOLF DAY 2018</h1>
    <p class="venue">Mount Ashcombe Golf Club</p>

    <div class="badge">
      <div class="badge-fun">A FUN</div>
      <div class="badge-day">DAY OUT</div>
    </div>

    <p class="function-note">A combined Harlowe<br>Old Scholars &nbsp;and Parents<br>&amp; Friends Function</p>

    <h2 class="event-date"><span class="day">MONDAY</span> <span class="num">22nd</span> <span class="month">OCTOBER</span> <span class="year">2018</span></h2>
    <p class="arrival">8.45am Arrival</p>

    <section class="sessions">
      <div class="session session-experienced">
        <span class="session-label">EXPERIENCED GOLFERS</span>
        <p class="session-detail">9am Shot gun Start for<br>18 hole players</p>
      </div>
      <div class="session session-beginner">
        <span class="session-label">BEGINNER GOLFERS</span>
        <p class="session-detail">11.30am to 12.30pm with<br>a Golf Pro for non-Golfers</p>
      </div>
    </section>

    <footer class="save-band">SAVE THE DATE</footer>
  </main>
</body>
</html>
```